Website Design

I require a website to be built around a CMS for a commercial client, an SME in the construction industry
I am happy to approach this 2 ways - either a full site redesign and build around a well known CMS by the successful candidate. Or a page template designed which I can then duplicate and use with a light CMS - I have enough coding experience to implement this myself.
I require a html/css file as the final piece of work,
Updates
Hi,
This is the site to be redesigned:
http://www.verntowers.co.uk/
As you can see it is quite dated.
The design should be quite focused on the images and photos of the products.
2 designs which were reject can be seen here:
verntowers.quillpixel.co.uk
verntowers2.quillpixel.co.uk
This is the clients main competitor: http://www.pelicanreach.com/ - They are keen to have a site which is 'better' than this one.
Hope this info helps. The site will include a lightbox gallery to focus on products, please bare this is mind when submitting your designs.
Reason: Need a higher number of designs to take to the client.
We are happy just to accept PSD designs if you believe the budget is too low for a HTML design. Please get in touch if you require more info.
Please can you use the customers logo from the website in designs. Thanks
Reason: Need more designers!
Target Market(s)
Industrial/Construction Sector
Industry/Entity Type
Construction
Requirements
Must have
- final design must be in html

```html
<!DOCTYPE html>
<html lang="en">
<head>
<meta charset="utf-8">
<title>Vern Towers</title>
<link rel="stylesheet" href="https://fonts.googleapis.com/css2?family=Ubuntu:wght@400;500;700&family=Arimo:wght@400;700&display=swap">
<style>
:root{
  --blue:#0a6bb3;
  --blue-dark:#053d7a;
  --blue-light:#1b8fd8;
  --grey-text:#555;
  --dark-text:#333;
  --line:#d8d8d8;
  --panel:#f3f3f3;
  --white:#fff;
}
*{margin:0;padding:0;box-sizing:border-box}
html,body{width:976px;height:1200px;overflow:hidden}
body{position:relative;background:var(--white);font-family:Arimo,Arial,sans-serif;color:var(--grey-text)}
.abs{position:absolute}
.sky{left:0;top:0;width:976px;height:377px;background:linear-gradient(180deg,#1a87cf 0%,#0e63ad 60%,#06458a 100%)}
.page{left:85px;top:100px;width:806px;height:978px;background:var(--white);box-shadow:0 0 6px rgba(0,0,0,.15)}
.header-curve{left:0;top:0;width:976px;height:110px}
.logo{left:94px;top:22px;display:flex;align-items:center;gap:8px}
.logo-dot{width:52px;height:52px;border-radius:50%;background:#4d7fb0}
.logo-name{font-family:Ubuntu,sans-serif;font-weight:700;color:#666;font-size:32px;line-height:.95;letter-spacing:1px}
.logo-name small{display:block;font-size:17px;letter-spacing:5px;font-weight:700}
.crew{left:520px;top:6px;width:200px;height:92px;background:linear-gradient(180deg,#dfe8ee,#b9c6cf);border-radius:40px 40px 0 0}
.call{left:728px;top:22px;display:flex;align-items:center;gap:6px;color:var(--white);font-family:Ubuntu,sans-serif;white-space:nowrap}
.call-text{font-size:15px;line-height:1.25;text-align:center}
.call-text b{display:block;font-weight:400;font-size:15px}
.nav{left:89px;top:99px;width:792px;height:29px;border:1px solid var(--line);border-radius:8px;background:linear-gradient(#fff,#ececec);display:flex;align-items:center;padding-left:8px}
.nav a{font-size:11px;color:#444;text-decoration:none;padding:0 13px;border-right:1px solid #ddd;line-height:22px}
.nav a.active{background:linear-gradient(#1e8fd6,#0a5ea8);color:#fff;border-radius:12px;padding:0 14px;border:none;margin-right:8px}
.nav-tag{position:absolute;right:12px;top:7px;font-family:Ubuntu,sans-serif;font-weight:700;font-size:12px;color:var(--blue);letter-spacing:.5px}
.hero-frame{left:89px;top:140px;width:573px;height:281px;background:#e6e6e6;border:1px solid #ccc}
.hero{left:94px;top:144px;width:563px;height:272px;background:linear-gradient(135deg,#f3d6a6,#d9a865 55%,#8a6a4a)}
.thumbs{left:677px;top:140px;width:207px;height:282px;background:#d6d6d6;border:1px solid #c4c4c4}
.thumb{left:682px;width:196px;height:86px;overflow:hidden;font-family:Ubuntu,sans-serif;color:#fff}
.thumb .ph{width:100%;height:100%;background:linear-gradient(160deg,#b89a72,#6d5a44)}
.thumb.t2 .ph{background:linear-gradient(160deg,#a2673d,#5b3a27)}
.thumb.t3 .ph{background:linear-gradient(180deg,#9fb3c4,#5f7a5a)}
.thumb .cap{position:absolute;left:0;right:0;bottom:0;padding:2px 3px 6px;background:linear-gradient(transparent,rgba(0,0,0,.45))}
.thumb .cap b{display:block;font-weight:500;font-size:13px}
.thumb .cap span{font-size:10px}
h2.about{left:98px;top:452px;font-family:Ubuntu,sans-serif;font-size:18px;font-weight:700;color:#777;border-bottom:1px solid #999;padding-bottom:1px}
h2.about em{font-style:normal;font-weight:500;color:var(--blue)}
.about-text{left:98px;top:480px;width:532px;font-size:9.3px;line-height:14.6px;text-align:justify;letter-spacing:.2px}
.about-text b{color:var(--dark-text)}
.worker{left:98px;top:549px;width:218px;height:84px;border-radius:6px;background:linear-gradient(135deg,#8da2b0,#3b4650 60%,#d2b45a)}
.worker-text{left:327px;top:555px;width:303px;font-size:9.3px;line-height:16.2px;text-align:justify;letter-spacing:.2px}
.worker-text b{color:var(--dark-text)}
.quick{left:91px;top:660px;width:539px;height:68px;background:var(--panel);border:1px solid #e0e0e0;border-radius:10px}
.quick a,.col li{position:absolute;font-size:10.5px;color:#666;text-decoration:none;letter-spacing:.2px}
.quick a::before,.col li::before{content:"";position:absolute;left:-14px;top:3px;border-left:4px solid var(--blue);border-top:3.5px solid transparent;border-bottom:3.5px solid transparent}
.col{top:769px;width:128px}
.col h3{font-family:Ubuntu,sans-serif;font-weight:500;font-size:15px;color:var(--blue)}
.col .pic{position:absolute;top:17px;width:127px;height:63px;border:1px solid #ccc;padding:5px;background:#fff}
.col .pic div{width:100%;height:100%}
.col ul{list-style:none}
.col li{left:14px;white-space:nowrap}
.col .more{position:absolute;top:239px;left:4px;font-size:10px;color:#444;white-space:nowrap}
.divider{top:762px;width:0;height:283px;border-left:1px dotted #bbb}
.office{left:651px;top:457px;width:227px;height:215px;border-radius:10px;background:linear-gradient(180deg,#168ad3,#0a4f96);color:#fff}
.office h3{position:absolute;left:11px;top:11px;font-family:Ubuntu,sans-serif;font-weight:400;font-size:17px}
.office .item{position:absolute;left:6px;display:flex;gap:10px}
.office .ph{width:72px;height:54px;border:2px solid #fff;background:linear-gradient(180deg,#7fb2da,#8a6a4a)}
.office p{width:131px;font-size:9.6px;line-height:13px;text-align:justify}
.btn{position:absolute;left:149px;top:188px;width:68px;height:17px;border-radius:9px;background:#fff;color:var(--blue);font-size:10px;text-align:center;line-height:17px}
.blog{left:656px;top:693px;width:218px;height:252px;border:1px solid #ccc;border-radius:6px;background:#fff;box-shadow:0 2px 3px rgba(0,0,0,.1)}
.blog h3{height:30px;background:linear-gradient(#fff,#e8e8e8);border-bottom:1px solid #ddd;border-radius:6px 6px 0 0;font-family:Ubuntu,sans-serif;font-weight:400;font-size:15px;color:#333;padding:7px 0 0 17px}
.post{position:absolute;left:18px;width:186px;font-size:9.1px;line-height:10.6px;color:#333}
.post a{display:block;color:var(--blue);font-weight:700;letter-spacing:.5px;margin-bottom:3px}
.post span{color:var(--blue);text-decoration:underline}
a.visit{position:absolute;left:18px;top:235px;font-size:9.3px;color:var(--blue)}
.soc{position:absolute;top:235px;width:12px;height:12px}
.pay{left:671px;top:968px;width:190px;height:76px;border:1px solid #ddd;background:#fff}
.pay h4{text-align:center;font-weight:400;font-size:10px;color:var(--blue);margin-top:-6px;background:#fff;width:88px;margin-left:51px}
.card{position:absolute;width:34px;height:21px;border:1px solid #ccc;background:#f4f4f4}
.card i{position:absolute;inset:4px;border-radius:2px}
.footer{left:0;top:1078px;width:976px;height:122px;background:linear-gradient(180deg,#0b62ab,#064a8f)}
.foot-logo{left:114px;top:1078px;width:208px;height:91px;background:#fff;border-radius:0 0 104px 104px;display:flex;justify-content:center;padding-top:16px}
.foot-logo .logo-name{font-size:24px}
.foot-logo .logo-name small{font-size:12px;letter-spacing:3px}
.foot-logo .logo-dot{width:36px;height:36px}
.foot-nav{left:342px;top:1092px;font-size:10.5px;color:#fff;font-weight:700}
.foot-nav a{color:#fff;text-decoration:none}
.foot-nav i{font-style:normal;margin:0 11px}
.copy{left:351px;top:1115px;font-size:9px;color:#6cc3f2}
.copy b{font-weight:400;color:#bfe4fb}
.vline{left:794px;top:1102px;width:1px;height:85px;background:#2b8bd2}
.follow{left:809px;top:1097px;color:#fff;font-family:Ubuntu,sans-serif;font-size:14px}
.social{left:809px;font-size:10px;color:#bfe4fb;display:flex;align-items:center;gap:9px}
.social i{width:20px;height:20px;border-radius:50%;background:#e9f3fb}
</style>
</head>
<body>
<div class="abs sky"></div>
<div class="abs page"></div>
<svg class="abs header-curve" viewBox="0 0 976 110" aria-hidden="true">
  <path d="M99 8 H320 C350 8 355 30 375 48 C395 66 420 70 470 70 H870 C882 70 891 78 891 88 V110 H85 V22 C85 14 91 8 99 8Z" fill="#fff"/>
</svg>
<div class="abs logo"><span class="logo-dot"></span><div class="logo-name">VERN<small>TOWERS</small></div></div>
<div class="abs crew" role="img" aria-label="Photo of two construction workers in hard hats holding plans"></div>
<div class="abs call">
  <svg width="48" height="38" viewBox="0 0 52 40" aria-hidden="true"><path d="M4 14 C8 4 44 4 48 14 L44 20 L36 17 L36 12 C28 9 24 9 16 12 L16 17 L8 20Z" fill="#e8eef4"/><path d="M14 20 H38 L44 36 H8Z" fill="#e8eef4"/><circle cx="26" cy="28" r="5" fill="#9fb4c8"/></svg>
  <div class="call-text"><b>Call Now:</b>(01632) 960418</div>
</div>
<nav class="abs nav">
  <a class="active" href="#">Home</a><a href="#">Services</a><a href="#">Hoists</a><a href="#">Examples</a><a href="#">Blog</a><a href="#" style="border:none">Contact</a>
  <span class="nav-tag">VERN SCAFFOLD MANUFACTURE</span>
</nav>

<div class="abs hero-frame"></div>
<div class="abs hero" role="img" aria-label="Photo of a builder in a hard hat reading plans inside a timber house frame"></div>
<div class="abs thumbs"></div>
<div class="abs thumb" style="top:146px"><div class="ph" role="img" aria-label="Photo of workers on a timber roof frame"></div><div class="cap"><b>No Power Emergency Descent</b><span>Lorem Ipsum is simply dummy</span></div></div>
<div class="abs thumb t2" style="top:237px"><div class="ph" role="img" aria-label="Photo of builders on a brick site"></div><div class="cap"><b>No Power Emergency Descent</b><span>Lorem Ipsum is simply dummy</span></div></div>
<div class="abs thumb t3" style="top:329px"><div class="ph" role="img" aria-label="Photo of workers on a rooftop over a city"></div><div class="cap"><b>No Power Emergency Descent</b><span>Lorem Ipsum is simply dummy</span></div></div>

<h2 class="abs about"><em>About</em> Vern Towers</h2>
<p class="abs about-text"><b>Lorem Ipsum is simply dummy text of the printing and typesetting industry. Lorem Ipsum has been the industry's standard dummy text ever since the 1500s,</b> when an unknown printer took a galley of type and scrambled it to make a type specimen book. It has survived not only five centuries, but also the leap into electronic typesetting, remaining essentially unchanged.</p>
<div class="abs worker" role="img" aria-label="Photo of a technician in a hard hat working on equipment"></div>
<p class="abs worker-text"><b>Lorem Ipsum is simply dummy text of the printing</b> and typesetting industry. Lorem Ipsum has been the industry's standard dummy text ever since the 1500s, when an unknown printer took a galley of type and scrambled it to make</p>

<div class="abs quick">
  <a href="#" style="left:34px;top:20px">Scafffold Manufacture</a>
  <a href="#" style="left:230px;top:20px">Mast Climber</a>
  <a href="#" style="left:429px;top:20px">Statistics</a>
  <a href="#" style="left:34px;top:49px">Fallarescue</a>
  <a href="#" style="left:230px;top:49px">Examples of our work</a>
  <a href="#" style="left:429px;top:49px">Safety First</a>
</div>

<div class="abs divider" style="left:230px"></div>
<div class="abs divider" style="left:366px"></div>
<div class="abs divider" style="left:502px"></div>

<section class="abs col" style="left:98px">
  <h3>Industries</h3>
  <div class="pic"><div role="img" aria-label="Photo of an industrial building by a river" style="background:linear-gradient(180deg,#8fb4d8,#7a8a5a 70%,#3f5a6b)"></div></div>
  <ul><li style="top:104px">Scafffold Manufacture</li><li style="top:124px">Fallarescue</li><li style="top:144px">Mast Climber</li><li style="top:163px">Examples of our work</li><li style="top:183px">Statistics</li><li style="top:203px">Safety First</li></ul>
  <span class="more">----------View More----------</span>
</section>
<section class="abs col" style="left:235px">
  <h3>Products</h3>
  <div class="pic"><div role="img" aria-label="Photo of a crane at dusk" style="background:linear-gradient(180deg,#3b4a6a,#c29a3a 75%,#222)"></div></div>
  <ul><li style="top:104px">Scafffold Manufacture</li><li style="top:124px">Fallarescue</li><li style="top:144px">Mast Climber</li><li style="top:163px">Examples of our work</li><li style="top:183px">Statistics</li><li style="top:203px">Safety First</li></ul>
  <span class="more">----------View More----------</span>
</section>
<section class="abs col" style="left:371px">
  <h3>Services</h3>
  <div class="pic"><div role="img" aria-label="Photo of a worker on scaffolding against a building" style="background:linear-gradient(180deg,#cfcfcf,#9a9a9a)"></div></div>
  <ul><li style="top:104px">Scafffold Manufacture</li><li style="top:124px">Fallarescue</li><li style="top:144px">Mast Climber</li><li style="top:163px">Examples of our work</li><li style="top:183px">Statistics</li><li style="top:203px">Safety First</li></ul>
  <span class="more">----------View More----------</span>
</section>
<section class="abs col" style="left:507px">
  <h3>Technologies</h3>
  <div class="pic"><div role="img" aria-label="Photo of a hard hat on technical plans" style="background:linear-gradient(135deg,#3a6fb5,#d9b84a 45%,#c9c9d6)"></div></div>
  <ul><li style="top:104px">Scafffold Manufacture</li><li style="top:124px">Fallarescue</li><li style="top:144px">Mast Climber</li><li style="top:163px">Examples of our work</li><li style="top:183px">Statistics</li><li style="top:203px">Safety First</li></ul>
  <span class="more">----------View More----------</span>
</section>

<aside class="abs office">
  <h3>Visit Our Office</h3>
  <div class="item" style="top:44px"><div class="ph" role="img" aria-label="Photo of a building under construction"></div><p><b>Lorem Ipsum is simply dummy text</b> of the printing and typesetting industry. Lorem Ipsum has.</p></div>
  <div class="item" style="top:114px"><div class="ph" role="img" aria-label="Photo of a building under construction"></div><p><b>Lorem Ipsum is simply dummy text</b> of the printing and typesetting industry. Lorem Ipsum has.</p></div>
  <span class="btn">Readmore</span>
</aside>

<aside class="abs blog">
  <h3>Blog Feed</h3>
  <div class="post" style="top:50px"><a href="#">10 Tips to fix those drips</a>Lorem ipsum dolor sit amet, consecte-tur adipiscing elit. Curabitur vel pellen-tesque nulla. <span>Read More</span></div>
  <div class="post" style="top:110px"><a href="#">When an Emergency arises</a>Lorem ipsum dolor sit amet, consecte-tur adipiscing elit. Curabitur vel pellen-tesque nulla. <span>Read More</span></div>
  <div class="post" style="top:169px"><a href="#">Cheap solutions</a>Lorem ipsum dolor sit amet, consecte-tur adipiscing elit. Curabitur vel pellen-tesque nulla. <span>Read More</span></div>
  <a class="visit" href="#">Visit Our Blog</a>
  <span class="soc" style="left:165px;background:#3b5b98"></span>
  <span class="soc" style="left:181px;background:#2aa3d8"></span>
  <span class="soc" style="left:197px;background:#f08a24"></span>
</aside>

<div class="abs pay">
  <h4>Payment Method</h4>
  <span class="card" style="left:14px;top:17px"><i style="background:#9cb3d6"></i></span>
  <span class="card" style="left:54px;top:17px"><i style="background:#2b4f9a"></i></span>
  <span class="card" style="left:97px;top:17px"><i style="background:#e35a2a"></i></span>
  <span class="card" style="left:139px;top:17px"><i style="background:#d58a3a"></i></span>
  <span class="card" style="left:14px;top:46px"><i style="background:#2a6fb0"></i></span>
  <span class="card" style="left:54px;top:46px"><i style="background:#222"></i></span>
  <span class="card" style="left:97px;top:46px"><i style="background:#c9d4e6"></i></span>
  <span class="card" style="left:139px;top:46px"><i style="background:#6a9a5a"></i></span>
</div>

<footer class="abs footer"></footer>
<div class="abs foot-logo"><div class="logo"><span class="logo-dot"></span><div class="logo-name">VERN<small>TOWERS</small></div></div></div>
<div class="abs foot-nav"><a href="#">Home</a><i>|</i><a href="#">Services</a><i>|</i><a href="#">Hoists</a><i>|</i><a href="#">Examples</a><i>|</i><a href="#">Blog</a><i>|</i><a href="#">Contact</a></div>
<div class="abs copy">Copyright © 2011 <b>Vern Towers</b> Corporation</div>
<div class="abs vline"></div>
<div class="abs follow">Follow Us On:</div>
<div class="abs social" style="top:1123px"><i></i>Linkbook</div>
<div class="abs social" style="top:1151px"><i></i>Chirper</div>
</body>
</html>
```